Micro Markets Vending business needs a web design

I purchased a logo through MarkFoundry and asked them to design my website but was told they couldn't and that I needed to contact you.
I was building a website through Plinth using AI and liked what they had created verbiage-wise but I can't figure out how to finish it the way I would like it. Will send screen shots of what was written, and subsequently used in my slogan under my logo. Would like to use the colors in my logo for my website.
About the company:
TW Vending, LLC offers micro market vending machines. Swipe your card, open the doors, take what you want. Can be customized by size for the space, and items for sale within the machines. Pictures of the machines are attached as examples.
I don't need a Testimonials page right now since we are a new company, but will need to add one at some point.
I also like the idea of a contact us button, as shown in the last picture (although it says subscribe). We do not have any emails set up as of yet. Haven't figured out how to do that, but will.
Just let me know what files you need from MarkFoundry for my logo.
Target Market(s)
Apartment complexes, Buildings, Hotels, Gyms, etc
Industry/Entity Type
Vending Machines
Number of Pages Required
1 page
Font styles to use
Other font styles liked:
- Your choice on font style that complements our logo font.

```html
<!DOCTYPE html>
<html lang="en">
<head>
<meta charset="utf-8">
<title>TW Vending, LLC — Micro Market Vending</title>
<link rel="stylesheet" href="https://fonts.googleapis.com/css2?family=Archivo+Black&family=Poppins:wght@400;500;600;700&display=swap">
<style>
:root{
  --green:#3f9b3a;
  --green-dark:#2c7a2a;
  --lime:#8dc63f;
  --ink:#1e241e;
  --text:#3b3f3b;
  --muted:#6c716c;
  --soft:#f2f3f2;
  --line:#dfe2df;
  --white:#ffffff;
  --black:#070807;
  --photo-a:#2b3b46;
  --photo-b:#7d8e95;
}
*{margin:0;padding:0;box-sizing:border-box}
html,body{width:1200px;height:3484px;overflow:hidden}
body{font-family:"Poppins",sans-serif;color:var(--text);background:var(--white);font-size:15px;line-height:1.6}
h1,h2,h3{font-family:"Archivo Black",sans-serif;color:var(--ink);font-weight:400;text-transform:uppercase}
.brand{display:flex;align-items:center;gap:12px;font-family:"Poppins",sans-serif;font-weight:700;font-size:24px;color:var(--green)}
.brand-mark{width:34px;height:34px;background:var(--green)}
.btn{display:inline-block;padding:12px 30px;border-radius:30px;font-weight:600;font-size:14px;text-transform:uppercase;color:var(--white);background:var(--green);text-decoration:none;letter-spacing:.5px}
.btn-dark{background:var(--ink)}
.photo{background:linear-gradient(135deg,var(--photo-a),var(--photo-b))}

/* header */
.site-header{height:112px;display:flex;align-items:center;justify-content:space-between;padding:0 40px 0 60px;position:relative}
.header-right{display:flex;flex-direction:column;align-items:flex-end;gap:14px}
.topline{display:flex;gap:40px;font-size:13px;font-weight:600;color:var(--ink)}
.topline span{display:flex;align-items:center;gap:8px}
.topline svg{width:18px;height:18px}
.main-nav{display:flex;gap:40px}
.main-nav a{font-size:14px;font-weight:500;color:var(--ink);text-decoration:none;text-transform:uppercase;padding-bottom:4px}
.main-nav a.active{color:var(--green);border-bottom:2px solid var(--green)}

/* hero */
.hero{height:608px;position:relative;overflow:hidden}
.hero-photo{position:absolute;inset:0}
.hero-panel{position:absolute;inset:0 auto 0 0;width:620px;background:linear-gradient(160deg,var(--lime),var(--green) 70%);clip-path:polygon(0 0,100% 0,82% 100%,0 100%);padding:110px 0 0 60px}
.hero-panel h1{color:var(--white);font-size:44px;line-height:1.12;width:470px}
.hero-panel p{color:var(--white);font-size:15px;margin:22px 0 30px;width:420px}

/* discover */
.discover{height:620px;position:relative}
.framed{position:absolute}
.framed .frame-back{position:absolute;border-radius:26px;background:var(--green)}
.framed .frame-lime{position:absolute;border-radius:26px;background:var(--lime)}
.framed .photo{position:absolute;border-radius:22px;inset:0}
.discover .framed{left:140px;top:100px;width:420px;height:400px}
.discover .frame-back{left:-18px;top:-18px;width:200px;height:200px}
.discover .frame-lime{right:-18px;bottom:-18px;width:200px;height:200px}
.discover-copy{position:absolute;left:625px;top:100px;width:470px}
.discover-copy h2{font-size:34px;margin-bottom:16px}
.discover-copy p{margin-bottom:18px}
.discover-copy .lead{color:var(--green);font-weight:600;margin-bottom:2px}
.discover-copy strong{color:var(--ink)}

/* why */
.why{height:640px;background:var(--soft);text-align:center;padding-top:70px}
.why h2{font-size:34px}
.why-intro{width:800px;margin:14px auto 50px;font-size:14px}
.features{display:flex;justify-content:center;gap:80px}
.feature{width:300px}
.feature-icon{width:130px;height:130px;margin:0 auto 24px}
.feature h3{font-family:"Poppins",sans-serif;font-weight:700;font-size:17px}
.feature .sub{color:var(--green);font-weight:600;font-size:14px;margin-bottom:10px}
.feature p{font-size:14px}

/* about */
.about{height:580px;position:relative}
.about-copy{position:absolute;left:110px;top:150px;width:470px}
.about-copy h2{font-size:34px;margin-bottom:20px}
.about-copy p{margin-bottom:18px}
.about .framed{left:650px;top:90px;width:420px;height:390px}
.about .frame-back{right:-18px;top:-18px;width:200px;height:200px}
.about .frame-lime{left:-18px;bottom:-18px;width:200px;height:200px}

/* contact */
.contact{height:540px;background:var(--soft);position:relative}
.contact h2{position:absolute;left:490px;top:60px;font-size:34px}
.contact-info{position:absolute;left:140px;top:150px}
.info-row{display:flex;align-items:center;gap:20px;margin-bottom:40px}
.info-icon{width:62px;height:62px;border-radius:50%;border:3px solid var(--green);display:flex;align-items:center;justify-content:center}
.info-icon svg{width:26px;height:26px}
.info-row h4{font-size:14px;font-weight:700;color:var(--ink);text-transform:uppercase}
.info-row p{font-size:14px;line-height:1.5}
.contact-form{position:absolute;left:480px;top:125px;width:580px;display:grid;grid-template-columns:1fr 1fr;gap:14px}
.field{height:50px;background:var(--white);border:1px solid var(--line);border-radius:4px;padding:14px;font-size:13px;color:var(--muted);box-shadow:0 4px 10px rgba(0,0,0,.08)}
.field.full{grid-column:1/3;height:120px}
.contact-form .btn{grid-column:1/2;justify-self:start;margin-top:6px;padding:10px 32px}

/* footer */
.site-footer{height:384px;background:var(--black);color:var(--white);text-align:center;padding-top:90px;position:relative}
.site-footer .brand{justify-content:center;color:var(--lime);font-size:28px}
.footer-nav{display:flex;justify-content:center;gap:90px;margin:80px 0 22px}
.footer-nav a{color:var(--white);text-decoration:none;font-size:14px;text-transform:uppercase}
.footer-rule{width:1040px;height:1px;background:#333;margin:0 auto 20px}
.copyright{font-size:13px}
.lang{position:absolute;right:40px;bottom:34px;font-size:13px;font-weight:600}
</style>
</head>
<body>

<header class="site-header">
  <div class="brand"><span class="brand-mark"></span>TW Vending, LLC</div>
  <div class="header-right">
    <div class="topline">
      <span><svg viewBox="0 0 24 24"><circle cx="12" cy="12" r="12" fill="#3f9b3a"/><path d="M8 6l2 3-1.3 1.3a8 8 0 0 0 5 5L15 14l3 2-1 2.5c-5 0-10-5-10-10z" fill="#fff"/></svg>+1 555 010 0200</span>
      <span><svg viewBox="0 0 24 24"><circle cx="12" cy="12" r="12" fill="#3f9b3a"/><path d="M12 5a4.5 4.5 0 0 0-4.5 4.5C7.5 13 12 19 12 19s4.5-6 4.5-9.5A4.5 4.5 0 0 0 12 5zm0 6.3a1.8 1.8 0 1 1 0-3.6 1.8 1.8 0 0 1 0 3.6z" fill="#fff"/></svg>TW VENDING UNITED STATE.</span>
    </div>
    <nav class="main-nav">
      <a class="active" href="#home">Home</a>
      <a href="#about">About Us</a>
      <a href="#services">Our Services</a>
      <a href="#why">Why Choose Us</a>
      <a href="#contact">Contact Us</a>
    </nav>
  </div>
</header>

<section class="hero" id="home">
  <div class="hero-photo photo" role="img" aria-label="Photo of glass-door micro market vending coolers stocked with drinks and snacks in an office"></div>
  <div class="hero-panel">
    <h1>If only vending machines dispensed opportunities like they do snacks.</h1>
    <p>TW Vending, LLC offers micro market vending machines. Swipe your card, open the doors, take what you want.</p>
    <a class="btn btn-dark" href="#contact">Get Started</a>
  </div>
</section>

<section class="discover" id="services">
  <div class="framed">
    <span class="frame-back"></span><span class="frame-lime"></span>
    <div class="photo" role="img" aria-label="Photo of a micro market vending machine filled with snacks and drinks"></div>
  </div>
  <div class="discover-copy">
    <h2>Discover Our Range</h2>
    <p class="lead">Welcome to TW Vending,</p>
    <p>where convenience meets customization.</p>
    <p>Our micro market vending machines in <strong>Greater Houston, TX</strong>, offer a variety of <strong>snacks and drinks</strong> tailored to your preferences.</p>
    <p>Swipe your credit card, open the doors, and indulge in what you desire.</p>
    <a class="btn" href="#about">Read More</a>
  </div>
</section>

<section class="why" id="why">
  <h2>Why Choose Us</h2>
  <p class="why-intro">TW Vending stands out for its commitment to quality, convenience, and customization. We prioritize customer preferences and aim to provide a seamless vending experience.</p>
  <div class="features">
    <div class="feature">
      <svg class="feature-icon" viewBox="0 0 130 130"><circle cx="65" cy="65" r="52" fill="#8a8f8a"/><path d="M10 80a58 58 0 0 0 110 0" fill="none" stroke="#3f9b3a" stroke-width="8" stroke-linecap="round"/><path d="M45 66l14 14 27-30" fill="none" stroke="#fff" stroke-width="8" stroke-linecap="round" stroke-linejoin="round"/></svg>
      <h3>Quality Products</h3>
      <p class="sub">Fresh and Varied Selection</p>
      <p>Our vending machines are stocked with a diverse range of snacks and drinks, ensuring that there's something for everyone.</p>
    </div>
    <div class="feature">
      <svg class="feature-icon" viewBox="0 0 130 130"><circle cx="65" cy="65" r="52" fill="#3f9b3a"/><path d="M10 80a58 58 0 0 0 110 0" fill="none" stroke="#8a8f8a" stroke-width="8" stroke-linecap="round"/><rect x="42" y="48" width="46" height="32" rx="5" fill="none" stroke="#fff" stroke-width="6"/><line x1="42" y1="58" x2="88" y2="58" stroke="#fff" stroke-width="6"/></svg>
      <h3>Convenience</h3>
      <p class="sub">Easy Access Anytime</p>
      <p>With TW Vending, snack time is just a swipe away. Our machines are strategically located for your convenience, providing quick and access to your favorite treats.</p>
    </div>
    <div class="feature">
      <svg class="feature-icon" viewBox="0 0 130 130"><circle cx="65" cy="65" r="52" fill="#8a8f8a"/><path d="M10 80a58 58 0 0 0 110 0" fill="none" stroke="#3f9b3a" stroke-width="8" stroke-linecap="round"/><circle cx="65" cy="62" r="16" fill="none" stroke="#fff" stroke-width="7"/><path d="M65 36v8M65 80v8M39 62h8M83 62h8M47 44l6 6M77 74l6 6M83 44l-6 6M53 74l-6 6" stroke="#fff" stroke-width="6" stroke-linecap="round"/></svg>
      <h3>Customization</h3>
      <p class="sub">Fresh and Varied Selection</p>
      <p>Personalize your snacking experience with TW Vending. Choose from a wide selection of snacks and drinks to create one that suits your unique preferences.</p>
    </div>
  </div>
</section>

<section class="about" id="about">
  <div class="about-copy">
    <h2>About TW Vending, LLC</h2>
    <p>At TW Vending, we are dedicated to revolutionizing the vending experience. Our mission is to provide a convenient way for you to access your favorite snacks and drinks in a hassle-free manner.</p>
    <p>With a focus on customer satisfaction, we ensure that our products are always fresh and our machines are well-maintained. Experience the future of vending with TW Vending, LLC.</p>
    <a class="btn" href="#contact">Explore Now</a>
  </div>
  <div class="framed">
    <span class="frame-back"></span><span class="frame-lime"></span>
    <div class="photo" role="img" aria-label="Photo of stocked micro market coolers in a building lobby"></div>
  </div>
</section>

<section class="contact" id="contact">
  <h2>Contact Us</h2>
  <div class="contact-info">
    <div class="info-row">
      <div class="info-icon"><svg viewBox="0 0 24 24"><path d="M6 3l3 4.5-1.8 1.8a11 11 0 0 0 7.5 7.5L16.5 15 21 18l-1.5 3C11 21 3 13 3 4.5z" fill="#3f9b3a"/></svg></div>
      <div><h4>Phone:</h4><p>+1 555 010 0200</p></div>
    </div>
    <div class="info-row">
      <div class="info-icon"><svg viewBox="0 0 24 24"><path d="M12 2a7 7 0 0 0-7 7c0 5.3 7 13 7 13s7-7.7 7-13a7 7 0 0 0-7-7zm0 9.5a2.5 2.5 0 1 1 0-5 2.5 2.5 0 0 1 0 5z" fill="#3f9b3a"/></svg></div>
      <div><h4>Address:</h4><p>1480 W. Orchard Ave. #210<br>Riverton, CA 90000</p></div>
    </div>
  </div>
  <form class="contact-form">
    <div class="field">First Name</div>
    <div class="field">Last Name</div>
    <div class="field">Phone Number</div>
    <div class="field">Email</div>
    <div class="field full">Message</div>
    <a class="btn" href="#contact">Submit</a>
  </form>
</section>

<footer class="site-footer">
  <div class="brand"><span class="brand-mark"></span>TW Vending, LLC</div>
  <nav class="footer-nav">
    <a href="#home">Home</a>
    <a href="#about">About Us</a>
    <a href="#services">Our Services</a>
    <a href="#why">Why Choose Us</a>
    <a href="#contact">Contact Us</a>
  </nav>
  <div class="footer-rule"></div>
  <p class="copyright">COPYRIGHT@2024 TW VENDING. ALL RIGHTS RESERVED</p>
  <span class="lang">EN</span>
</footer>

</body>
</html>
```